School website design - Technology and the arts

We will need a new or updated design that incorporates the following features:
-Reactive design that changes with the needs of the device.
-Static Background - only content scrolls
-Static Menu - similar to the Pressly Harbor Lantern theme
-Alert box for important notices (closings/emergency use only) that doesn’t display unless active
-Margins must be wider than “standard pressly theme” (fits the entire display at any resolution, doesn’t just center a columned design)
-Features an image scroll on the front page to show our current works/progress. (only if the screen is big enough). Should have swipe capability
-We must have a place on the front page to display the current school news as well as a location to display current events with a poster (see current webdesign for example)
-Uses the school colors (green and gold/yellow) in a way that is pleasing to the eye.
-Unique design to our school that is very clean and modern.
-Events need to be able to pop-out when you mouseover in a desktop environment. Example: http://skinvault.example/category/pressly/creative (mouse over a theme and it shows additional information about it without a refresh)
-Custom Admin panel to easily updated the news and events section.
-Notes: We are currently using some free icons that we found to make the current site look not so boring since we do not have a lot of content on each page. We would like to step away from that and are open to suggestions. Possibly something like http://vormlab.example/demo/?theme=arch under the services section but smaller.
-Notes 2: We have plenty of pictures of our building and activities that can be used as a background, etc.
-We are open to new ideas and suggestions.

Our current website is https://www.kelmont-academy.example to get an idea on how we manage our current site.

```html
<!DOCTYPE html>
<html lang="en">
<head>
<meta charset="utf-8">
<title>Kelmont Regional Academy</title>
<link rel="stylesheet" href="https://fonts.googleapis.com/css2?family=Tinos&family=Raleway:ital,wght@0,400;0,600;0,700;1,600;1,700&family=Montserrat:wght@500;600&display=swap">
<style>
:root{
  --green:#2f6b35;
  --green-dark:#0c3e10;
  --orange:#f0a232;
  --gold:#f2c33a;
  --ink:#333;
  --muted:#777;
  --rule:#e2e2e2;
  --serif:'Tinos',serif;
  --sans:'Raleway',sans-serif;
  --nav:'Montserrat',sans-serif;
}
*{margin:0;padding:0;box-sizing:border-box}
html,body{width:870px;height:1200px;overflow:hidden;background:#fff}
body{position:relative;font-family:var(--sans);color:var(--ink)}
.abs{position:absolute}

/* header */
.site-header{position:absolute;left:0;top:0;width:870px;height:101px;border-bottom:2px solid #eee;background:#fff}
.brand-mark{left:64px;top:24px;display:flex;align-items:center;gap:6px;font-family:var(--serif);font-size:15px;color:var(--green)}
.brand-mark i{width:14px;height:14px;border-radius:50%;background:var(--gold);display:block}
.site-title{left:186px;top:27px;font-family:var(--serif);font-size:16.5px;letter-spacing:.2px;color:#222}
.site-sub{left:186px;top:47px;font-size:9.5px;color:#444}
.utility{right:62px;top:10px;display:flex;gap:8px;font-size:7.5px;color:#555;font-family:var(--nav)}
.utility span{display:flex;align-items:center;gap:3px}
.utility svg{width:8px;height:8px}
.search{left:660px;top:45px;width:148px;height:17px;border-bottom:1px solid #ccc;border-right:1px solid #ccc;font-size:7px;color:#777;padding:5px 0 0 3px}
.search svg{position:absolute;right:3px;top:3px;width:10px;height:10px}
.main-nav{left:235px;top:79px;width:572px;display:flex;justify-content:space-between;font-family:var(--nav);font-weight:600;font-size:7.3px;color:#222}
.main-nav .active{color:var(--orange);position:relative}
.main-nav .active::after{content:"";position:absolute;left:-3px;right:-3px;top:18px;height:2px;background:var(--orange)}

/* hero */
.hero{left:0;top:110px;width:870px;height:229px;background:linear-gradient(100deg,#5f8f3a 0%,#8fb25a 35%,#4f7a30 65%,#39632a 100%)}
.hero-copy{left:522px;top:168px;width:280px;color:#fff}
.hero-copy h1{font-family:var(--serif);font-weight:400;font-size:24px;line-height:1}
.hero-copy p{font-size:10.3px;line-height:13px;margin-top:8px}
.btn{display:inline-block;margin-top:9px;background:var(--orange);color:#fff;font-family:var(--serif);font-size:12px;width:129px;height:25px;text-align:center;line-height:25px}
.dots{left:438px;top:320px;display:flex;gap:4px}
.dots i{width:7px;height:7px;background:var(--orange);display:block}
.dots i:first-child{background:#fff}

.band{left:0;top:339px;width:870px;height:39px;background:#f4f4f2;border-bottom:1px solid #e8e8e8}
.band::before{content:"";position:absolute;left:180px;right:110px;top:13px;height:1px;background:#ddd}

/* services */
.services{left:0;top:378px;width:870px;height:210px;background:linear-gradient(180deg,#f6f7f3,#fbfbf9 60%,#f1f2ee)}
.service{position:absolute;top:397px;width:190px;text-align:center}
.service .ring{width:88px;height:88px;border-radius:50%;border:2.5px solid var(--green);margin:0 auto;display:flex;align-items:center;justify-content:center;background:#fff}
.service .ring.fill{background:var(--green)}
.service .ring svg{width:32px;height:32px}
.service h3{font-family:var(--serif);font-weight:400;font-size:12.5px;margin-top:12px;color:#222}
.service p{font-size:8.5px;color:var(--muted);line-height:11px;margin-top:4px}

/* welcome / mission */
.section-title{font-family:var(--serif);font-size:14px;color:#555;letter-spacing:.3px;padding-bottom:4px;border-bottom:1px solid #999}
.welcome-title{left:65px;top:611px;width:193px}
.welcome-photo{left:64px;top:643px;width:343px;height:112px;background:linear-gradient(90deg,#2a2a2e,#4a3a44 50%,#2e2a30)}
.divider-v{width:1px;background:var(--rule)}
.mission-title{left:471px;top:611px;width:194px}
.mission-text{left:471px;top:641px;width:335px;font-size:8.6px;line-height:11.2px;color:#555}
.learn{left:471px;top:708px;font-size:9.5px;font-weight:700;font-style:italic;color:var(--green)}
.divider-h{height:1px;background:var(--rule)}

/* columns */
.col-head{display:flex;align-items:center;gap:6px;font-family:var(--serif);font-size:12px;color:#555;letter-spacing:.3px}
.col-head svg{width:17px;height:17px}
.date{width:24px;height:24px;background:var(--green-dark);color:#fff;font-size:8px;font-weight:700;text-align:center;line-height:10px;padding-top:2px}
.news-title{font-size:12px;font-style:italic;font-weight:600;color:var(--green-dark)}
.news-sub{font-size:7.7px;color:#555;line-height:10px}
.more{font-family:var(--nav);font-size:6.7px;color:var(--green);font-weight:500}
.sep{height:1px;background:var(--rule)}
.thumb{width:33px;height:32px;background:linear-gradient(135deg,#5a5660,#c9b9a8)}
.event-text{font-size:7.7px;color:#666;line-height:10.5px;width:150px}
.program-photo{left:590px;top:827px;width:146px;height:81px;border:2px solid var(--gold);background:linear-gradient(120deg,#c9a98a,#e8e2d8 50%,#9d8a7a)}
.list h4{font-size:8px;font-weight:400;color:#333;margin-bottom:2px}
.list li{list-style:none;font-size:6.6px;font-weight:600;color:var(--green);line-height:9.3px}
.list li::before{content:"→| ";color:#777;font-weight:400}

/* footer */
.site-footer{left:0;top:1006px;width:870px;height:194px;background:var(--green-dark);color:#fff}
.foot-head{font-size:10px;font-weight:700;font-style:italic}
.foot-links li{list-style:none;font-size:7.5px;line-height:16.4px;letter-spacing:.2px}
.support-box{left:511px;top:1047px;width:114px;height:75px;background:#fff}
.support-box p{position:absolute;left:10px;top:12px;font-size:8.8px;line-height:12px;color:#555}
.support-box b{color:#222;font-weight:700}
.support-box em{font-style:normal;color:var(--gold);font-weight:700}
.support-photo{position:absolute;right:0;top:0;width:50px;height:75px;background:linear-gradient(180deg,#e9e9ea,#cfd3d8)}
.foot-brand{left:740px;top:1070px;display:flex;align-items:center;gap:5px;font-family:var(--serif);font-size:13px;color:#cfd9cf}
.foot-brand i{width:10px;height:10px;border-radius:50%;background:#cfd9cf;display:block}
.social{left:743px;top:1123px;display:flex;gap:7px}
.social i{width:13px;height:13px;border-radius:50%;display:block}
.copyright{left:0;width:870px;top:1175px;text-align:center;font-size:7.3px;color:#d8e2d8}
</style>
</head>
<body>

<header class="site-header">
  <div class="abs brand-mark"><i></i>KELMONT</div>
  <div class="abs site-title">KELMONT REGIONAL ACADEMY</div>
  <div class="abs site-sub">for the arts &amp; technology | 240 N. Lantern Ave, 10452 555.014.0270</div>
  <div class="abs utility">
    <span><svg viewBox="0 0 10 10"><path d="M1 5L5 1l4 4M2 4v5h6V4" fill="none" stroke="#555"/></svg>KRA EMAIL</span><span>|</span>
    <span><svg viewBox="0 0 10 10"><rect x="1" y="2" width="8" height="7" fill="none" stroke="#555"/><path d="M1 4h8" stroke="#555"/></svg>CALENDARS</span><span>|</span>
    <span><svg viewBox="0 0 10 10"><rect x="2" y="1" width="6" height="8" fill="none" stroke="#555"/><circle cx="5" cy="4" r="1.2" fill="#555"/></svg>CONTACT US</span>
  </div>
  <div class="abs search">Enter keyword
    <svg viewBox="0 0 10 10"><circle cx="4.2" cy="4.2" r="3" fill="none" stroke="#444"/><path d="M6.4 6.4L9 9" stroke="#444"/></svg>
  </div>
  <nav class="abs main-nav">
    <span class="active">HOME</span><span>ABOUT KRA</span><span>STUDENTS/PARENTS</span><span>FACULTY/STAFF</span><span>DOCUMENTS/FORMS</span><span>PROGRAMS OF STUDY</span><span>SERVICES</span>
  </nav>
</header>

<div class="abs hero" role="img" aria-label="Smiling students with backpacks and books on a sunny green campus"></div>
<div class="abs hero-copy">
  <h1>Duis autem vel eum iriure</h1>
  <p>Lorem ipsum dolor sit amet, consectetuer adipiscing elit, sed diam nonummy nibh euismod tincidunt ut laoreet dolore magna aliquam erat volutpat.</p>
  <span class="btn">READ MORE...</span>
</div>
<div class="abs dots"><i></i><i></i><i></i><i></i></div>
<div class="abs band"></div>

<section class="abs services" role="img" aria-label="Faded photo of a bright classroom behind the service links"></section>
<div class="service" style="left:145px">
  <div class="ring fill"><svg viewBox="0 0 32 32"><path d="M3 12l13-6 13 6-13 6z" fill="none" stroke="#fff" stroke-width="1.8"/><path d="M9 15v6c2 3 12 3 14 0v-6" fill="none" stroke="#fff" stroke-width="1.8"/></svg></div>
  <h3>School Counseling</h3><p>Changing your schedule, career<br>planning, testing</p>
</div>
<div class="service" style="left:339px">
  <div class="ring"><svg viewBox="0 0 32 32"><rect x="4" y="6" width="24" height="16" fill="none" stroke="#2f6b35" stroke-width="1.8"/><path d="M11 27h10M16 22v5" stroke="#2f6b35" stroke-width="1.8"/></svg></div>
  <h3>Information Technology</h3><p>Help and support for technology<br>services.</p>
</div>
<div class="service" style="left:534px">
  <div class="ring"><svg viewBox="0 0 32 32"><path d="M3 7c5-1 9-1 13 2 4-3 8-3 13-2v18c-5-1-9-1-13 2-4-3-8-3-13-2z M16 9v18" fill="none" stroke="#2f6b35" stroke-width="1.8"/><path d="M6 12h7M6 16h7M6 20h7M19 12h7M19 16h7M19 20h7" stroke="#2f6b35"/></svg></div>
  <h3>Library and Media Center</h3><p>Checking out a book, device, or just come<br>to visit in a nice quiet environment.</p>
</div>

<h2 class="abs section-title welcome-title">WELCOME TO OUR SCHOOL</h2>
<div class="abs welcome-photo" role="img" aria-label="Crowd of cheering students at a school pep rally"></div>
<div class="abs divider-v" style="left:440px;top:640px;height:120px"></div>
<h2 class="abs section-title mission-title">OUR MISSION</h2>
<p class="abs mission-text">The Kelmont Regional Academy for the Arts and Technology provides gifted and talented students a differentiated and rigorous education, cultivates a supportive environment that inspires unique artistic and technological visions, promotes cultural tolerance, nurtures community partnerships, and produces active, engaged citizens.</p>
<div class="abs learn">Learn More...</div>
<div class="abs divider-h" style="left:145px;top:778px;width:580px"></div>

<!-- latest news -->
<div class="abs col-head" style="left:76px;top:799px"><svg viewBox="0 0 17 17"><rect x="3" y="1.5" width="11" height="14" fill="none" stroke="#777"/><path d="M5 5h7M5 8h7M5 11h7" stroke="#777"/></svg>LATEST NEWS</div>
<div class="abs date" style="left:76px;top:831px">APR<br>07</div>
<div class="abs news-title" style="left:111px;top:824px">Varsity Boys’</div>
<div class="abs news-sub" style="left:111px;top:840px">Home Soccer match vs<br>Brookfield</div>
<div class="abs more" style="left:240px;top:855px">READ MORE</div>
<div class="abs sep" style="left:64px;top:870px;width:220px"></div>
<div class="abs date" style="left:76px;top:883px">APR<br>07</div>
<div class="abs news-title" style="left:111px;top:881px">Varsity Girls’</div>
<div class="abs news-sub" style="left:113px;top:898px;font-size:8.6px;line-height:11px">Home Tennis match vs<br>Marlow</div>
<div class="abs more" style="left:242px;top:912px">READ MORE</div>
<div class="abs sep" style="left:64px;top:927px;width:220px"></div>
<div class="abs date" style="left:76px;top:939px">APR<br>07</div>
<div class="abs news-sub" style="left:113px;top:946px;font-size:8.6px">State Placement Test</div>
<div class="abs more" style="left:244px;top:976px">READ MORE</div>

<div class="abs divider-v" style="left:311px;top:818px;height:145px"></div>

<!-- upcoming events -->
<div class="abs col-head" style="left:343px;top:799px"><svg viewBox="0 0 17 17"><rect x="1.5" y="3" width="13" height="11" fill="none" stroke="#2f6b35"/><path d="M1.5 6h13M5 1.5v3M11 1.5v3" stroke="#2f6b35"/><circle cx="13" cy="13" r="3" fill="#fff" stroke="#2f6b35"/><path d="M13 11.5v3M11.5 13h3" stroke="#2f6b35"/></svg>UPCOMING EVENTS</div>
<div class="abs thumb" style="left:342px;top:826px" role="img" aria-label="Event poster"></div>
<div class="abs event-text" style="left:380px;top:825px">cultivates asupportiveen viroent that inspires unique artistic and technological.....</div>
<div class="abs more" style="left:445px;top:860px">READ MORE</div>
<div class="abs thumb" style="left:342px;top:879px" role="img" aria-label="Event poster"></div>
<div class="abs event-text" style="left:380px;top:878px">cultivates asupportiveen viroent that inspires unique artistic and technological.....</div>
<div class="abs more" style="left:445px;top:913px">READ MORE</div>
<div class="abs thumb" style="left:342px;top:934px" role="img" aria-label="Event poster"></div>
<div class="abs event-text" style="left:380px;top:933px">cultivates asupportiveen viroent that inspires unique artistic and technological.....</div>
<div class="abs more" style="left:445px;top:975px">READ MORE</div>

<div class="abs divider-v" style="left:558px;top:818px;height:145px"></div>

<!-- programs of study -->
<div class="abs col-head" style="left:595px;top:798px"><svg viewBox="0 0 17 17"><rect x="1" y="2" width="4" height="13" fill="#2f6b35"/><rect x="6" y="2" width="4" height="13" fill="#2f6b35"/><rect x="11" y="3" width="4" height="12" fill="#2f6b35" transform="rotate(-12 13 9)"/></svg>PROGRAMS OF STUDY</div>
<div class="abs program-photo" role="img" aria-label="Students working together around a classroom table"></div>
<div class="abs list" style="left:592px;top:915px"><h4>Focus Areas</h4><ul><li>Dance</li><li>Literary Arts</li><li>Music</li><li>Technology</li><li>Theatre Arts</li><li>Visual Arts</li></ul></div>
<div class="abs list" style="left:675px;top:915px"><h4>Study Programs</h4><ul><li>English</li><li>Health and PE</li><li>Math</li><li>Science</li><li>Social Sciences</li><li>World Languages</li></ul></div>

<footer class="abs site-footer">
  <div class="abs foot-head" style="left:66px;top:15px">QUICK LINKS</div>
  <ul class="abs foot-links" style="left:66px;top:35px"><li>HOME</li><li>ADMISSIONS</li><li>STAFF DIRECTORY</li><li>INFORMATION TECHNOLOGY</li><li>LIBRARY</li><li>GRADEPORTAL (TEACHERS)</li></ul>
  <ul class="abs foot-links" style="left:278px;top:35px"><li>KRA EMAIL</li><li>ONLINE SCHOOL PAYMENTS</li><li>ATHLETICS</li><li>DOCUMENTS/FORMS</li><li>CONTACT US</li><li>GRADEPORTAL (PARENTS/STUDENTS)</li></ul>
  <div class="abs foot-head" style="left:510px;top:15px">SUPPORT</div>
  <div class="abs divider-h" style="left:64px;top:156px;width:740px;background:#2c5a2f"></div>
  <div class="abs copyright" style="top:169px">Copyright © 2014 Kelmont Regional Academy</div>
</footer>
<div class="abs support-box">
  <p><b>CALL FOR<br>HELP!</b><br>Show your<br>support for<br><em>KRA!</em></p>
  <div class="support-photo" role="img" aria-label="Support agent wearing a headset"></div>
</div>
<div class="abs foot-brand"><i></i>KELMONT</div>
<div class="abs social"><i style="background:#3b5998"></i><i style="background:#1da1f2"></i><i style="background:#d34836"></i></div>

</body>
</html>
```